Bramble Roofing Website Relaunch

We require a re-launch of our website, We are a longrun roofing company based in New Zealand, we are rapidly expanding and require a more professionally presented website our current website is www.brambleroofing.co.nz we want something modern, masculine and communicates a "strong" "superior" image, we already have a logo which I have attached we use the orange and silver one as you will see on our current website

Industry/Entity Type

It Company

Number of Pages Required

1 page

Colors
f37122
f78f20
000000
1b1b1b
474747
d3d3d3
f5f5f5

Requirements
Must have
• Images of our work
• Email and Mobile Contact Details
• Link to Follow us page
• Who We Are, What We Do
• Certified Trade Craftsman Logo
• Our Logo

```html
<!DOCTYPE html>
<html lang="en">
<head>
<meta charset="utf-8">
<title>Bramble Roofing</title>
<link href="https://fonts.googleapis.com/css2?family=Roboto:wght@300;400;500;700;900&display=swap" rel="stylesheet">
<style>
:root{
  --orange:#f37122;
  --orange-light:#f78f20;
  --black:#000000;
  --ink:#1b1b1b;
  --charcoal:#474747;
  --silver:#d3d3d3;
  --mist:#f5f5f5;
  --white:#ffffff;
  --footer:#3b3531;
}
*{box-sizing:border-box;margin:0;padding:0}
html,body{width:1200px;height:3550px;overflow:hidden}
body{font-family:"Roboto",Arial,sans-serif;color:var(--charcoal);background:var(--white);position:relative}
.abs{position:absolute}

/* top bar */
.topbar{position:absolute;left:0;top:0;width:1200px;height:42px;background:var(--orange);color:var(--white)}
.topbar .contact{position:absolute;top:4px;display:flex;align-items:center;gap:8px}
.topbar .contact .ico{width:30px;height:30px;border-radius:50%;border:2px solid var(--white);display:flex;align-items:center;justify-content:center}
.topbar .contact small{display:block;font-size:9px;font-weight:700;letter-spacing:.5px}
.topbar .contact strong{display:block;font-size:14px;font-weight:700}
.topbar .contact span{display:block;font-size:12px}
.social{position:absolute;left:966px;top:0;width:74px;height:30px;background:#3b5998;color:var(--white);font-size:13px;font-weight:700;display:flex;align-items:center;justify-content:center}

/* nav */
.nav{position:absolute;left:0;top:42px;width:1200px;height:58px;background:var(--white);border-bottom:1px solid var(--silver)}
.brand{position:absolute;left:160px;top:12px;display:flex;align-items:center;gap:10px}
.brand .mark{width:30px;height:30px;background:var(--orange)}
.brand .name{font-size:19px;font-weight:700;color:var(--orange);letter-spacing:.5px}
.menu{position:absolute;left:664px;top:14px;display:flex;gap:0}
.menu a{display:block;padding:8px 17px;font-size:12px;font-weight:500;color:var(--ink);text-decoration:none;letter-spacing:.3px}
.menu a.active{color:var(--orange);border:1px solid var(--silver);border-bottom:3px solid var(--orange)}

/* hero */
.hero{position:absolute;left:0;top:100px;width:1200px;height:520px;background:linear-gradient(160deg,#5e6e80 0%,#3b434f 45%,#232830 100%);overflow:hidden}
.hero h1{position:absolute;left:0;width:1200px;text-align:center;font-weight:900;font-size:50px;letter-spacing:2px;line-height:1}
.hero h1.l1{top:130px;color:var(--white)}
.hero h1.l2{top:186px;color:var(--orange-light)}
.hero p{position:absolute;left:390px;top:248px;width:420px;text-align:center;color:var(--white);font-size:14px;line-height:1.55}
.btn{display:inline-flex;align-items:center;gap:10px;background:var(--orange);color:var(--white);font-size:11px;font-weight:700;letter-spacing:.5px;text-decoration:none;justify-content:center}
.btn .arr{width:14px;height:14px;border-radius:50%;background:var(--white);display:flex;align-items:center;justify-content:center}
.hero .btn{position:absolute;left:511px;top:342px;width:178px;height:42px}
.slide-arrow{position:absolute;top:245px;width:50px;height:50px;background:var(--orange);transform:rotate(45deg);display:flex;align-items:center;justify-content:center}
.slide-arrow span{transform:rotate(-45deg);color:var(--white);font-size:9px;font-weight:700;letter-spacing:1px}

/* section headings */
.eyebrow{position:absolute;left:0;width:1200px;text-align:center;color:var(--orange);font-size:18px;font-weight:300;letter-spacing:1px}
.heading{position:absolute;left:0;width:1200px;text-align:center;color:var(--charcoal);font-size:38px;font-weight:700;letter-spacing:1px}

/* about */
.worker{position:absolute;left:178px;top:650px;width:380px;height:405px;background:radial-gradient(ellipse at 45% 40%,#f0b02a 0%,#9aa3ad 40%,#e9ecef 75%,#ffffff 100%)}
.about-eyebrow{position:absolute;left:625px;top:695px;color:var(--orange);font-size:17px;font-weight:300;letter-spacing:1px}
.about-title{position:absolute;left:625px;top:714px;color:var(--charcoal);font-size:38px;font-weight:700;letter-spacing:1px}
.about-text{position:absolute;left:625px;top:790px;width:410px;font-size:12px;line-height:1.75;color:var(--charcoal)}
.bullets{position:absolute;left:625px;top:930px;list-style:none}
.bullets li{font-size:12px;line-height:22px;display:flex;align-items:center;gap:12px}
.bullets li::before{content:"";width:8px;height:8px;border-radius:50%;border:2px solid var(--orange)}

/* service cards */
.card{position:absolute;width:277px;height:182px;border:1px solid #e6e6e6;background:var(--white)}
.card.active{border:2px solid var(--orange)}
.card h3{position:absolute;left:0;top:124px;width:100%;text-align:center;font-size:14px;font-weight:700;color:var(--ink);letter-spacing:.5px}
.card.active h3{color:var(--orange)}
.diamond{position:absolute;width:144px;height:144px;transform:rotate(45deg);border:5px solid var(--white);box-shadow:0 0 0 1px #e0e0e0}
.card.active+.diamond, .diamond.hl{box-shadow:0 0 0 1px var(--orange)}
.card-btn{position:absolute;width:104px;height:33px;background:var(--charcoal)}
.card-btn.hot{background:var(--orange)}
.card-btn .arr svg path{fill:var(--charcoal)}
.card-btn.hot .arr svg path{fill:var(--orange)}

/* projects */
.projects{position:absolute;left:0;top:1941px;width:1200px;height:615px;background:linear-gradient(180deg,#eeeeee,#f5f5f5 50%,#ececec)}
.shot{position:absolute;width:277px;height:152px}
.shot-overlay{position:absolute;left:14px;top:10px;width:186px;height:120px;background:var(--orange);opacity:.92;display:flex;align-items:center;justify-content:center;color:var(--white);font-size:13px;font-weight:700;letter-spacing:.5px}

/* team */
.member{position:absolute;top:2852px;width:277px;height:237px;border:1px solid #e6e6e6;background:var(--white)}
.member.active{border:2px solid var(--orange)}
.member h4{position:absolute;left:0;top:116px;width:100%;text-align:center;font-size:14px;font-weight:700;color:var(--ink);letter-spacing:.5px}
.member.active h4{color:var(--orange)}
.member p{position:absolute;left:20px;top:138px;width:237px;text-align:center;font-size:10px;line-height:1.45;color:var(--charcoal)}
.portrait{position:absolute;width:136px;height:136px;transform:rotate(45deg);border:5px solid var(--white);box-shadow:0 0 0 1px #e0e0e0}

/* contact strip */
.footer{position:absolute;left:0;top:3188px;width:1200px;height:296px;background:linear-gradient(180deg,#4a423c,var(--footer))}
.strip{position:absolute;left:161px;top:3131px;width:876px;height:112px;background:linear-gradient(90deg,var(--orange-light),#e9a04a 50%,var(--orange-light));display:flex}
.strip div{flex:1;text-align:center;color:var(--white);padding-top:28px;border-right:1px solid rgba(255,255,255,.35)}
.strip div:last-child{border-right:0}
.strip h5{font-size:15px;font-weight:700;letter-spacing:.5px}
.strip p{font-size:18px;font-weight:300;margin-top:6px;line-height:1.15}
.fcol{position:absolute;top:3270px;color:var(--white)}
.fcol h6{font-size:14px;font-weight:700;letter-spacing:.5px;padding-bottom:10px;border-bottom:1px solid rgba(255,255,255,.2);width:276px}
.fcol p{font-size:11px;line-height:1.5;color:var(--silver);margin-top:12px;width:250px}
.fcol ul{list-style:none;margin-top:12px}
.fcol li{font-size:11px;color:var(--silver);line-height:25px;display:flex;align-items:center;gap:14px}
.fcol li::before{content:"";width:7px;height:7px;border-radius:50%;border:2px solid var(--white)}
.flogo{margin-top:18px;display:flex;align-items:center;gap:10px}
.flogo .mark{width:28px;height:28px;background:var(--silver)}
.flogo .name{font-size:18px;font-weight:700;color:var(--silver)}
.badge{width:110px;height:110px;border-radius:50%;background:var(--silver);opacity:.8;margin-top:14px}
.copyright{position:absolute;left:0;top:3484px;width:1200px;height:66px;background:#262220;color:var(--silver);font-size:11px;text-align:center;line-height:66px}
</style>
</head>
<body>

<header class="topbar">
  <div class="contact" style="left:160px">
    <div class="ico"><svg width="14" height="14" viewBox="0 0 24 24"><path fill="#fff" d="M6.6 10.8a15 15 0 0 0 6.6 6.6l2.2-2.2a1 1 0 0 1 1-.25 11.4 11.4 0 0 0 3.6.57 1 1 0 0 1 1 1V20a1 1 0 0 1-1 1A17 17 0 0 1 3 4a1 1 0 0 1 1-1h3.5a1 1 0 0 1 1 1c0 1.25.2 2.45.57 3.57a1 1 0 0 1-.25 1z"/></svg></div>
    <div><small>CALL US AT</small><strong>021 555 01842</strong></div>
  </div>
  <div class="contact" style="left:312px">
    <div class="ico"><svg width="14" height="14" viewBox="0 0 24 24"><path fill="#fff" d="M2 5h20v14H2zm2 2v.5l8 5 8-5V7l-8 5z"/></svg></div>
    <div><small>MAIL US AT</small><span>hello@brambleroofing.co.nz</span></div>
  </div>
  <a class="social">Follow us</a>
</header>

<nav class="nav">
  <div class="brand"><div class="mark"></div><div class="name">BRAMBLE ROOFING</div></div>
  <div class="menu">
    <a class="active">HOME</a><a>ABOUT</a><a>SERVICES</a><a>OUR WORK</a><a>CONTACT</a>
  </div>
</nav>

<section class="hero" role="img" aria-label="Roofers installing longrun iron roofing on a building against the sky">
  <h1 class="l1">DUIS EU GRAVIDA DUI</h1>
  <h1 class="l2">VITAE TINCIDUNT METUS</h1>
  <p>Lorem ipsum dolor sit amet, consectetur adipiscing elit. Curabitur vestibulum rhoncus ultrices. Vivamus tincidunt egestas magna. Ut commodo euismod fermentum. Duis porttitor dapibus magna</p>
  <a class="btn">GET THE FREE QUOTE <span class="arr"><svg width="8" height="8" viewBox="0 0 8 8"><path d="M2 1l4 3-4 3z" fill="#f37122"/></svg></span></a>
  <div class="slide-arrow" style="left:-8px"><span>PREV</span></div>
  <div class="slide-arrow" style="left:1158px"><span>NEXT</span></div>
</section>

<section class="about">
  <div class="worker" role="img" aria-label="Roofer in a hard hat holding a drill and hammer"></div>
  <div class="about-eyebrow">WELCOME TO</div>
  <h2 class="about-title">BRAMBLE ROOFING</h2>
  <p class="about-text">We are a local, family owned and operated company with over 18 years extensive experience in the roofing industry. Roofing not only Waikato and Auckland but surrounding areas also. We are committed to providing superior service to our customers regardless of how big or small your project is. Your satisfaction is our guarantee. We take pride in installing quality products, Offering a workmanship guarantee and manufacturers material warranties where applicable.</p>
  <ul class="bullets">
    <li>Proin ut eros mattis, luctus dolor ut, convallis enim.</li>
    <li>Aliquam auctor nisi et sem feugiat malesuada.</li>
    <li>Sed consequat felis vel diam eleifend facilisis.</li>
  </ul>
</section>

<section class="services">
  <div class="eyebrow" style="top:1136px">WHAT WE DO</div>
  <h2 class="heading" style="top:1152px">OUR SERVICES</h2>

  <div class="card" style="left:161px;top:1356px"><h3>NEW ROOFS AND RE-ROOFS</h3></div>
  <div class="diamond" style="left:228px;top:1234px;background:linear-gradient(135deg,#7ea3cf,#2f3d52 60%,#1d2430)" role="img" aria-label="New roof installation photo"></div>
  <a class="btn card-btn" style="left:248px;top:1521px">READ MORE <span class="arr"><svg width="8" height="8" viewBox="0 0 8 8"><path d="M2 1l4 3-4 3z"/></svg></span></a>

  <div class="card active" style="left:462px;top:1356px"><h3>METAL CLADDING</h3></div>
  <div class="diamond hl" style="left:529px;top:1234px;background:linear-gradient(135deg,#9bb0c4,#3f4a55 55%,#2a3036)" role="img" aria-label="Metal cladding photo"></div>
  <a class="btn card-btn hot" style="left:548px;top:1521px">READ MORE <span class="arr"><svg width="8" height="8" viewBox="0 0 8 8"><path d="M2 1l4 3-4 3z"/></svg></span></a>

  <div class="card" style="left:760px;top:1356px"><h3>SPOUTING AND METAL FASCIA</h3></div>
  <div class="diamond" style="left:827px;top:1234px;background:linear-gradient(135deg,#e5e7ea,#8e9399 55%,#3d4146)" role="img" aria-label="Spouting and fascia photo"></div>
  <a class="btn card-btn" style="left:847px;top:1521px">READ MORE <span class="arr"><svg width="8" height="8" viewBox="0 0 8 8"><path d="M2 1l4 3-4 3z"/></svg></span></a>

  <div class="card" style="left:161px;top:1683px"><h3>DOWN PIPES</h3></div>
  <div class="diamond" style="left:228px;top:1588px;background:linear-gradient(135deg,#c9b79c,#8a7258 55%,#4a3e33)" role="img" aria-label="Down pipes photo"></div>
  <a class="btn card-btn" style="left:248px;top:1850px">READ MORE <span class="arr"><svg width="8" height="8" viewBox="0 0 8 8"><path d="M2 1l4 3-4 3z"/></svg></span></a>

  <div class="card" style="left:462px;top:1683px"><h3>ALTERATIONS</h3></div>
  <div class="diamond" style="left:529px;top:1588px;background:linear-gradient(135deg,#7d93ad,#6b6458 55%,#3b3a36)" role="img" aria-label="Roof alterations photo"></div>
  <a class="btn card-btn" style="left:548px;top:1850px">READ MORE <span class="arr"><svg width="8" height="8" viewBox="0 0 8 8"><path d="M2 1l4 3-4 3z"/></svg></span></a>

  <div class="card" style="left:760px;top:1683px"><h3>SPOUTING AND METAL FASCIA</h3></div>
  <div class="diamond" style="left:827px;top:1588px;background:linear-gradient(135deg,#4d6784,#2a3444 55%,#161b22)" role="img" aria-label="Metal fascia photo"></div>
  <a class="btn card-btn" style="left:847px;top:1850px">READ MORE <span class="arr"><svg width="8" height="8" viewBox="0 0 8 8"><path d="M2 1l4 3-4 3z"/></svg></span></a>
</section>

<section class="projects">
  <div class="eyebrow" style="top:64px">OUR WORK</div>
  <h2 class="heading" style="top:80px">FEATURED PROJECTS</h2>

  <div class="shot" style="left:161px;top:182px;background:linear-gradient(180deg,#8fb4de 0%,#cfdce8 40%,#3a3c40 60%,#4f8a3a 85%)" role="img" aria-label="Completed house roof project"></div>
  <div class="shot" style="left:462px;top:182px;background:linear-gradient(180deg,#aab6c2,#6d7682)" role="img" aria-label="Roofing project photo"><div class="shot-overlay">VOLUTPAT TORTOR SIT</div></div>
  <div class="shot" style="left:760px;top:182px;background:linear-gradient(180deg,#9aa3ab 0%,#4d5258 50%,#35393e)" role="img" aria-label="Long metal roof project"></div>
  <div class="shot" style="left:161px;top:355px;background:linear-gradient(180deg,#a9c6e4 0%,#d5dde3 35%,#3b3e43 60%,#5d6a4c)" role="img" aria-label="Residential roof project"></div>
  <div class="shot" style="left:462px;top:355px;background:linear-gradient(180deg,#7aa3d1 0%,#b7c7d6 40%,#8a7a68 70%,#6e6a5e)" role="img" aria-label="New build roofing project"></div>
  <div class="shot" style="left:760px;top:355px;background:linear-gradient(180deg,#5f8fd0 0%,#b5c9de 50%,#7e8388 80%)" role="img" aria-label="Steel frame construction project"></div>

  <a class="btn" style="position:absolute;left:548px;top:542px;width:104px;height:33px">READ MORE <span class="arr"><svg width="8" height="8" viewBox="0 0 8 8"><path d="M2 1l4 3-4 3z" fill="#f37122"/></svg></span></a>
</section>

<section class="team">
  <div class="eyebrow" style="top:2628px">OUR PEOPLES</div>
  <h2 class="heading" style="top:2644px">MEET THE TEAM</h2>

  <div class="member" style="left:161px">
    <h4>OWEN "THE BOSS"</h4>
    <p>Owen started Bramble Roofing fulfilling his dream of owning his own business after 18+ years in the roofing industry. His focus, integrity and unrivalled level of expertise ensures he remains a leader in the industry, increasingly in demand and a reputable installer of choice.</p>
  </div>
  <div class="portrait" style="left:231px;top:2755px;background:linear-gradient(135deg,#d9c6a8,#9a7660 55%,#4e5a3e)" role="img" aria-label="Portrait of the company owner"></div>

  <div class="member active" style="left:462px">
    <h4>LIAM FLETCHER</h4>
    <p>Liam has been in the industry for 10+ years. Having entered into roofing straight from school. He has expertise in all roofing installations as well as experience in roofing installations in Australia. Liam is proficient in complex, creative finishing and flashing systems.</p>
  </div>
  <div class="portrait" style="left:532px;top:2755px;background:linear-gradient(135deg,#7fb36a,#c8d2d8 55%,#6d7c88)" role="img" aria-label="Portrait of a roofing installer"></div>

  <div class="member" style="left:760px">
    <h4>MARIA OKORO</h4>
    <p>Maria is Owen's wife and office manager, she works full time off site, with an employment history of 15+ years in the construction, materials handling equipment and project administration sectors. Her spare time is taken up managing Bramble Roofing, facilitating the daily.</p>
  </div>
  <div class="portrait" style="left:830px;top:2755px;background:linear-gradient(135deg,#dfe3e6,#a58d7a 55%,#5a5f66)" role="img" aria-label="Portrait of the office manager"></div>
</section>

<footer>
  <div class="footer" role="img" aria-label="Dark timber texture background"></div>
  <div class="strip">
    <div><h5>CALL US AT</h5><p>021 555 01842</p></div>
    <div><h5>EMAIL US AT</h5><p>hello@brambleroofing.co.nz</p></div>
    <div><h5>REACH US AT</h5><p>Proin ut eros mattis, luctus dolor ut, convallis enim.</p></div>
  </div>

  <div class="fcol" style="left:161px">
    <h6>ABOUT BRAMBLE ROOFING</h6>
    <div class="flogo"><div class="mark"></div><div class="name">BRAMBLE ROOFING</div></div>
    <p>Lorem ipsum is simply dummy text of the printing and typesetting industry. Lorem ipsum has been the industry's standard dummy text.</p>
  </div>
  <div class="fcol" style="left:462px">
    <h6>OUR SERVICES</h6>
    <ul>
      <li>New Roofs and Re-roofs</li>
      <li>Metal Cladding</li>
      <li>Spouting and Metal Fascia</li>
      <li>Down Pipes</li>
      <li>Alterations</li>
      <li>Extensions</li>
    </ul>
  </div>
  <div class="fcol" style="left:760px">
    <h6>CERTIFIED TRADE CRAFTSMAN</h6>
    <p>Pellentesque a nisi ut mauris iaculis luctus so sed mauris. Sed eget massa et erat rhoncus tincidunt.</p>
    <div class="badge" role="img" aria-label="Certified trade craftsman badge"></div>
  </div>

  <div class="copyright">© Copyright 2017 All Rights Reserved</div>
</footer>

</body>
</html>
```